Gablestone Inspections Business Card

I need a business card for my new company. The company is going to provide home inspections. The name of the company is Gablestone Inspections. I am not sure if I want a single sided card or a double. I have a logo already that I want to incorporate into the card design. I was wondering if I should incorporate a catch phrase on my card or not. If I did the phrase would be "Thorough Eyes on Every Corner of Your Home" but i am unsure how or if to use it on a card. The following information needs to be on the card.
Home Inspection
My Name: Tobias R. Fenwick Phone Number: 555-317-6420 Email: tfenwick@gablestoneinspections.com Website: www.gablestoneinspections.com NY HI License # 27300592415

```html
<!DOCTYPE html>
<html lang="en">
<head>
<meta charset="utf-8">
<title>Gablestone Inspections – Business Card</title>
<link href="https://fonts.googleapis.com/css2?family=Montserrat:wght@400;500;700;800&display=swap" rel="stylesheet">
<style>
  :root {
    --bg: #e6e8eb;
    --brand-blue: #0f6eb0;
    --brand-blue-deep: #0b5f9c;
    --brand-blue-emboss: #0c609b;
    --sky: #74c1ee;
    --ink: #1e1e1e;
    --white: #ffffff;
  }
  * { box-sizing: border-box; margin: 0; padding: 0; }
  html, body {
    width: 1200px; height: 1200px; overflow: hidden;
    background: var(--bg);
    font-family: "Montserrat", sans-serif;
  }
  .canvas {
    position: relative; width: 1200px; height: 1200px;
    display: flex; flex-direction: column; align-items: center; justify-content: center; gap: 48px;
  }
  .card {
    position: relative; width: 900px; height: 514px;
    border-radius: 30px; overflow: hidden;
    box-shadow: 0 10px 28px rgba(0,0,0,0.18);
  }

  /* Back side */
  .card-back {
    background: var(--brand-blue);
    display: flex; flex-direction: column; align-items: center; justify-content: center;
  }
  .back-wordmark {
    font-weight: 800; font-size: 48px; letter-spacing: 1px; white-space: nowrap;
    color: var(--brand-blue-emboss); text-transform: uppercase;
    display: flex; align-items: center; gap: 20px;
    margin-top: -40px;
  }
  .back-wordmark .mark-square {
    width: 34px; height: 34px; background: var(--brand-blue-emboss); flex: none;
  }
  .tagline {
    position: absolute; bottom: 82px; left: 0; right: 0; text-align: center;
    color: var(--white); font-weight: 700; font-size: 24px; letter-spacing: 0.5px;
  }

  /* Front side */
  .card-front { background: var(--white); }
  .front-content { position: absolute; left: 84px; top: 70px; }
  .front-wordmark {
    font-weight: 800; font-size: 40px; color: var(--brand-blue-deep); white-space: nowrap;
    text-transform: uppercase; display: flex; align-items: center; gap: 14px;
  }
  .front-wordmark .mark-square { width: 26px; height: 26px; background: var(--brand-blue-deep); flex: none; }
  .holder-name {
    margin-top: 54px; font-weight: 800; font-size: 38px; color: var(--brand-blue-deep);
  }
  .contact-list { list-style: none; margin-top: 30px; }
  .contact-list li {
    display: flex; align-items: center; gap: 18px;
    font-size: 22px; font-weight: 500; color: var(--ink); line-height: 1; margin-bottom: 16px;
  }
  .contact-list svg { width: 24px; height: 24px; flex: none; }
  .contact-list .license { padding-left: 42px; }
  .bottom-band {
    position: absolute; left: 0; right: 0; bottom: 0; height: 18px;
    background: var(--brand-blue-deep);
  }
  .corner-accent {
    position: absolute; right: 0; bottom: 18px; width: 240px; height: 10px;
    background: var(--sky);
  }
</style>
</head>
<body>
<main class="canvas">

  <section class="card card-back" aria-label="Card back">
    <div class="back-wordmark"><span class="mark-square"></span>Gablestone Inspections</div>
    <p class="tagline">Thorough Eyes on Every Corner of Your Home</p>
  </section>

  <section class="card card-front" aria-label="Card front">
    <div class="front-content">
      <div class="front-wordmark"><span class="mark-square"></span>Gablestone Inspections</div>
      <h1 class="holder-name">Tobias R. Fenwick</h1>
      <ul class="contact-list">
        <li>
          <svg viewBox="0 0 24 24" aria-hidden="true"><path fill="#0b5f9c" d="M6.6 10.8a15.2 15.2 0 0 0 6.6 6.6l2.2-2.2a1 1 0 0 1 1-.25 11.4 11.4 0 0 0 3.6.57 1 1 0 0 1 1 1V20a1 1 0 0 1-1 1A17 17 0 0 1 3 4a1 1 0 0 1 1-1h3.5a1 1 0 0 1 1 1c0 1.25.2 2.45.57 3.57a1 1 0 0 1-.25 1z"/></svg>
          555-317-6420
        </li>
        <li>
          <svg viewBox="0 0 24 24" aria-hidden="true"><rect x="2" y="5" width="20" height="14" rx="2" fill="#0b5f9c"/><path d="M3 6l9 7 9-7" fill="none" stroke="#fff" stroke-width="1.6"/></svg>
          tfenwick@gablestoneinspections.com
        </li>
        <li>
          <svg viewBox="0 0 24 24" aria-hidden="true"><circle cx="12" cy="12" r="10" fill="#0b5f9c"/><path d="M2 12h20M12 2c3 3 3 17 0 20M12 2c-3 3-3 17 0 20" fill="none" stroke="#fff" stroke-width="1.4"/></svg>
          www.gablestoneinspections.com
        </li>
        <li class="license">NY HI License # 27300592415</li>
      </ul>
    </div>
    <div class="corner-accent"></div>
    <div class="bottom-band"></div>
  </section>

</main>
</body>
</html>
```